Stationary design for new high end strategy and business consulting company

We need a stationary design (incorporating business card, letter head, consultant profile, envelope, invoice etc.) for a new company called VANTORA that is based in Australia.

Company provides high end strategy consulting/ advisory services - business insight - to the professional services, financial services, legal and health industries - in the areas of:
- strategy
- business transformation
- performance and profitability improvement
- commercial negotiation and procurement.

to enable companies to deliver an exceptional client experience for minimum cost, differentiate themselves in the market and maximize profitability

Design needs to be simple, stylish and sophisticated, bold and engaging. It should convey growth and prosperity; intelligent insight into how to make a company better and be more profitable; unique business insight.

Business cards should feature VANTORA prominently as well as our Director’s name “Marisol Pettigrew”

Other contact details are as follows:
Mob: 0472 618 304
Email: mapettigrew@vantorahq.com
Web: www.vantorahq.com

Colour pallet should incorporate lime green, dark greys, silver/ white

Target Market(s)

Law Firms
Banks, Investment Banks and Financial Services Companies
Healthcare companies that own hospitals, nursing homes, radiology and pathology services

Industry/Entity Type

Financial

Font styles to use
Sans Serif

Colors
add136
5c5c5c
e9e9e9

```html
<!DOCTYPE html>
<html lang="en">
<head>
<meta charset="utf-8">
<title>VANTORA Stationery</title>
<link rel="stylesheet" href="https://fonts.googleapis.com/css2?family=Raleway:wght@300;400&display=swap">
<style>
  :root {
    --mint: #4ae8c4;
    --ink: #5c5c5c;
    --ink-soft: #8a8a8a;
    --paper: #ffffff;
    --backdrop: #e9e9e9;
    --rule: #b5b5b5;
  }
  * { box-sizing: border-box; margin: 0; padding: 0; }
  html, body {
    width: 1200px; height: 994px; overflow: hidden;
    background: var(--backdrop);
    font-family: "Raleway", sans-serif;
    color: var(--ink);
  }
  .sheet { position: absolute; background: var(--paper); box-shadow: 0 2px 8px rgba(0,0,0,.12); }

  .wordmark { font-weight: 300; text-transform: uppercase; color: var(--ink); white-space: nowrap; line-height: 1; }

  /* Letterhead */
  .letterhead { left: 40px; top: 170px; width: 440px; height: 650px; padding: 48px 44px; }
  .letterhead .wordmark { text-align: right; font-size: 26px; letter-spacing: 8px; margin-right: -8px; }
  .letterhead-address { text-align: right; font-size: 9px; letter-spacing: 1px; line-height: 1.6; margin-top: 14px; color: var(--ink-soft); }
  .letter-body { margin-top: 60px; font-size: 11px; line-height: 1.8; color: var(--ink); }
  .letter-body p { margin-bottom: 16px; }

  /* Square contact card */
  .square-card { left: 510px; top: 170px; width: 310px; height: 310px; padding: 30px; }
  .square-card .wordmark { font-size: 30px; letter-spacing: 9px; margin-top: 90px; }
  .contact-list { position: absolute; left: 30px; bottom: 30px; list-style: none; font-size: 9px; letter-spacing: 2px; line-height: 1.9; text-transform: uppercase; }

  /* Business card */
  .business-card { left: 860px; top: 170px; width: 300px; height: 172px; padding: 34px 24px; }
  .business-card .wordmark { font-size: 24px; letter-spacing: 7px; }
  .holder-name { margin-top: 30px; font-size: 11px; font-weight: 400; letter-spacing: 5px; text-transform: uppercase; color: #333; }

  /* Postcard */
  .postcard { left: 510px; top: 520px; width: 650px; height: 325px; display: flex; }
  .postcard-face { width: 325px; height: 325px; background: var(--mint); display: flex; align-items: center; justify-content: center; }
  .postcard-face .wordmark { font-size: 28px; letter-spacing: 9px; margin-right: -9px; }
  .postcard-back { position: relative; flex: 1; }
  .address-lines { position: absolute; right: 34px; top: 160px; width: 190px; }
  .address-lines span { display: block; border-top: 1px solid var(--rule); margin-bottom: 28px; }
  .postcard-web { position: absolute; left: 0; right: 0; bottom: 28px; text-align: center; font-size: 9px; letter-spacing: 4px; text-transform: uppercase; }
</style>
</head>
<body>

<section class="sheet letterhead">
  <p class="wordmark">VANTORA</p>
  <p class="letterhead-address">Suite 12, 80 Harbour Road<br>Sydney NSW 2000</p>
  <div class="letter-body">
    <p>Dear Client,</p>
    <p>Thank you for meeting with our team this week. We have outlined the next steps for the strategy review below.</p>
    <p>Our advisors will share a draft plan by the end of the month for your comments.</p>
    <p>Kind regards,</p>
  </div>
</section>

<section class="sheet square-card">
  <p class="wordmark">VANTORA</p>
  <ul class="contact-list">
    <li>0472 618 304</li>
    <li>mapettigrew@vantorahq.com</li>
    <li>www.vantorahq.com</li>
  </ul>
</section>

<section class="sheet business-card">
  <p class="wordmark">VANTORA</p>
  <p class="holder-name">Marisol Pettigrew</p>
</section>

<section class="sheet postcard">
  <div class="postcard-face">
    <p class="wordmark">VANTORA</p>
  </div>
  <div class="postcard-back">
    <div class="address-lines"><span></span><span></span><span></span></div>
    <p class="postcard-web">www.vantorahq.com</p>
  </div>
</section>

</body>
</html>
```